New IT recruitment and consulting company need web logo.

We need a web logo design for a new company based in Scandinavia called "Relmo".
We work with recruitment and management consulting within HR and strategy mainly for the IT industry in Scandinavia. Long experience from recruitment and the IT industry.
We would like to see designs that use the color orange. The design should communicate trust, enthusiasm, success and energy.

Target Market(s)

CEO and line managers in the potential customer companies.

Industry/Entity Type

Management Consulting

Number of Pages Required

1 page

Font styles to use
Sans Serif

Requirements
Must have
• Modern web design.
Nice to have
• We would like to see designs that use the color orange.

```html
<!DOCTYPE html>
<html lang="en">
<head>
<meta charset="utf-8">
<title>Relmo — Recruitment &amp; Management Consulting</title>
<link rel="stylesheet" href="https://fonts.googleapis.com/css2?family=Raleway:wght@300;400;600;700;800&family=Open+Sans:ital,wght@0,400;0,600;0,700;1,400&display=swap">
<style>
:root{
  --orange:#e0531a;
  --orange-dark:#c9440f;
  --ink:#333333;
  --text:#5a5a5a;
  --muted:#8a8a8a;
  --line:#dddddd;
  --grey-bg:#f2f2f2;
  --footer:#2f2f2f;
  --footer-deep:#222222;
  --white:#ffffff;
}
*{box-sizing:border-box;margin:0;padding:0}
html,body{width:1200px;height:2166px;overflow:hidden}
body{position:relative;background:var(--white);font-family:"Open Sans",Arial,sans-serif;color:var(--text)}
.abs{position:absolute}

/* header */
.top-rule{left:0;top:0;width:1200px;height:4px;background:var(--orange)}
.site-header{left:0;top:4px;width:1200px;height:124px;background:var(--white)}
.brand{left:84px;top:44px;display:flex;align-items:center;gap:10px;font-family:"Raleway",sans-serif;font-weight:700;font-size:50px;color:var(--orange);letter-spacing:1px}
.brand-dot{width:14px;height:14px;border-radius:50%;background:var(--orange)}
.header-contact{left:866px;top:32px;display:flex;align-items:center;gap:8px}
.social-dot{width:30px;height:30px;border-radius:50%;background:var(--orange)}
.social-dot.alt{background:#8a8a8a}
.phone-chip{width:30px;height:30px;border-radius:50%;background:var(--orange);margin-left:14px;display:flex;align-items:center;justify-content:center}
.header-phone{font-size:14px;font-weight:600;color:var(--ink);white-space:nowrap}
.main-nav{left:618px;top:78px;display:flex;align-items:center;font-size:15px;color:var(--ink);white-space:nowrap}
.main-nav a{text-decoration:none;color:inherit;padding:0 22px;border-left:1px solid var(--line);line-height:18px;white-space:nowrap}
.main-nav a.active{background:linear-gradient(#e8652a,var(--orange-dark));color:var(--white);border:none;line-height:35px;padding:0 25px;margin-right:17px;border-radius:2px}
.main-nav a.active + a{border-left:none}

/* hero */
.hero{left:0;top:128px;width:1200px;height:515px;background:
  radial-gradient(ellipse 260px 300px at 890px 230px,rgba(90,200,255,.35),transparent 70%),
  linear-gradient(90deg,#5a4636 0%,#3b3430 35%,#1f2430 60%,#161b26 100%)}
.hero-title{left:87px;top:330px;color:var(--white);font-family:"Raleway",sans-serif;font-size:29px;line-height:36px;white-space:nowrap}
.hero-title strong{font-weight:700;display:block}
.hero-title span{font-weight:300;display:block;letter-spacing:1px}
.hero-text{left:89px;top:400px;width:460px;color:#eeeeee;font-size:14px;line-height:22px}
.hero-btn{left:89px;top:453px;width:134px;height:40px;background:var(--orange);color:var(--white);font-size:14px;display:flex;align-items:center;justify-content:center;border-radius:2px}
.hero-arrow{top:360px}

/* welcome */
.section-title{font-family:"Raleway",sans-serif;font-weight:800;color:var(--orange);font-size:29px;letter-spacing:.5px;white-space:nowrap}
.welcome-title{left:0;width:1200px;top:688px;text-align:center}
.title-rule{height:2px;background:#bdbdbd}
.welcome-rule{left:455px;top:733px;width:290px}
.welcome-text{left:125px;top:755px;width:950px;text-align:center;font-size:12px;line-height:24px}
.service{width:240px;text-align:center;top:838px}
.service-ring{width:118px;height:118px;border-radius:50%;border:1.5px solid #666;margin:0 auto;display:flex;align-items:center;justify-content:center}
.service-ring.featured{border-color:var(--orange)}
.service h3{font-family:"Open Sans",sans-serif;font-weight:400;font-size:16px;color:var(--ink);margin-top:18px;white-space:nowrap}
.service p{font-size:12px;line-height:21px;margin:10px auto 0;width:205px}

/* why / testimonials */
.band-grey{left:0;top:1121px;width:1200px;height:391px;background:var(--grey-bg)}
.why-text{left:87px;top:1242px;width:400px;font-size:12px;line-height:24px}
.check-list{list-style:none;font-size:12px;color:var(--text)}
.check-list li{display:flex;align-items:center;gap:10px;height:25px;white-space:nowrap}
.check{width:15px;height:15px;border-radius:50%;background:var(--orange);display:flex;align-items:center;justify-content:center}
.read-more{left:84px;top:1408px;color:var(--orange);font-size:13px;text-decoration:underline}
.quote{left:573px;top:1254px;width:500px;font-style:italic;font-size:11.5px;line-height:24.5px;color:var(--muted)}
.quote-mark{font-family:Georgia,serif;font-size:40px;color:#c8c8c8;line-height:1}
.avatar{left:557px;top:1341px;width:90px;height:90px;border-radius:50%;border:3px solid var(--white);box-shadow:0 0 0 1px #ddd;background:radial-gradient(circle at 50% 40%,#e7d7c7,#8899aa)}
.author{left:667px;top:1373px}
.author strong{display:block;color:var(--orange);font-size:11px;font-weight:700}
.author span{font-size:11px;color:var(--ink)}
.pager{left:973px;top:1389px;display:flex;gap:4px}
.pager i{width:12px;height:12px;border-radius:50%;background:#c4c4c4;display:block}

/* customers */
.customers-title{left:0;width:1200px;top:1569px;text-align:center}
.customers-rule{left:478px;top:1612px;width:244px}
.client{top:1639px;width:175px;height:97px;border:5px solid #f1f1f1;background:var(--white);display:flex;align-items:center;justify-content:center;font-weight:700;font-size:19px;color:#5c5c5c}
.carousel-arrow{top:1675px}

/* contact band */
.contact-band{left:0;top:1791px;width:1200px;height:63px;background:var(--orange);color:var(--white)}
.contact-item{top:1791px;height:63px;display:flex;align-items:center;gap:14px;color:var(--white);font-size:13px;white-space:nowrap}
.contact-ring{width:34px;height:34px;border:1.5px solid var(--white);border-radius:50%;display:flex;align-items:center;justify-content:center;flex:none}

/* footer */
.site-footer{left:0;top:1854px;width:1200px;height:266px;background:var(--footer)}
.footer-brand{left:84px;top:1915px;font-family:"Raleway",sans-serif;font-weight:700;font-size:50px;color:var(--white);display:flex;align-items:center;gap:10px}
.footer-brand .brand-dot{background:var(--white)}
.footer-about{left:84px;top:1995px;width:240px;color:#e6e6e6;font-size:12px;line-height:22px}
.footer-col-title{font-family:"Raleway",sans-serif;font-weight:400;font-size:19px;color:#eeeeee;letter-spacing:.5px;white-space:nowrap}
.footer-col-rule{height:1px;background:#777}
.footer-links{list-style:none;font-size:12px;color:#e6e6e6}
.footer-links li{height:30.5px;display:flex;align-items:center;gap:10px;white-space:nowrap}
.footer-links li::before{content:"›";font-size:14px;color:#bbb}
.footer-divider{top:1905px;width:1px;height:185px;background:#3f3f3f}
.map{left:878px;top:1932px;width:237px;height:150px;border:3px solid var(--white);background:linear-gradient(135deg,#f4efd8,#e9e3c2 50%,#dfe8d2)}
.legal-bar{left:0;top:2120px;width:1200px;height:46px;background:var(--footer-deep)}
.copyright{left:84px;top:2133px;color:#cfcfcf;font-size:12px}
.legal-social{left:1004px;top:2129px;display:flex;gap:8px}
.legal-social .social-dot{width:28px;height:28px}
</style>
</head>
<body>

<div class="abs top-rule"></div>
<header class="abs site-header"></header>
<div class="abs brand"><span>Relmo</span><span class="brand-dot"></span></div>

<div class="abs header-contact">
  <span class="social-dot"></span><span class="social-dot alt"></span><span class="social-dot"></span>
  <span class="phone-chip"><svg width="14" height="18" viewBox="0 0 14 18"><rect x="2" y="1" width="10" height="16" rx="2" fill="none" stroke="#fff" stroke-width="1.6"/><circle cx="7" cy="14" r="1" fill="#fff"/></svg></span>
  <span class="header-phone">(555)-310-2280</span>
</div>

<nav class="abs main-nav">
  <a class="active">Home</a><a>About us</a><a>Services</a><a>Solutions</a><a>Options</a>
</nav>

<section class="abs hero" role="img" aria-label="Businessman in a dark suit holding glowing people icons in cupped hands over a blurred city background"></section>
<h1 class="abs hero-title"><strong>RECRUITMENT &amp; MANAGEMENT</strong><span>CONSULTING</span></h1>
<p class="abs hero-text">Nemo enim ipsam voluptatem quia voluptas sit aspernatur aut odit aut fugit, sed quia consequuntur magni dolores</p>
<a class="abs hero-btn">Read more info</a>
<svg class="abs hero-arrow" style="left:32px" width="18" height="54" viewBox="0 0 18 54"><path d="M16 2 L3 27 L16 52" fill="none" stroke="#ddd" stroke-width="1.5"/></svg>
<svg class="abs hero-arrow" style="left:1148px" width="18" height="54" viewBox="0 0 18 54"><path d="M2 2 L15 27 L2 52" fill="none" stroke="#ddd" stroke-width="1.5"/></svg>

<h2 class="abs section-title welcome-title">WELCOME TO RELMO</h2>
<div class="abs title-rule welcome-rule"></div>
<p class="abs welcome-text">Lorem Ipsum is simply dummy text of the printing and typesetting industry. Lorem Ipsum has been the industry's standard dummy text ever since the 1500s, when an unknown printer took a galley of type and scrambled it to make a type specimen book.</p>

<div class="abs service" style="left:79px">
  <div class="service-ring"><svg width="56" height="56" viewBox="0 0 56 56" fill="none" stroke="#555" stroke-width="1.6"><path d="M28 14a11 11 0 0 0-6 20v5h12v-5a11 11 0 0 0-6-20z"/><path d="M23 43h10M24 47h8M28 4v5M12 10l4 4M44 10l-4 4M6 26h5M45 26h5"/></svg></div>
  <h3>Recruitment</h3><p>Pain can procure him some great pleasure. To take a trivial example, which of us ever takes</p>
</div>
<div class="abs service" style="left:339px">
  <div class="service-ring"><svg width="56" height="56" viewBox="0 0 56 56" fill="none" stroke="#555" stroke-width="1.6"><rect x="8" y="24" width="8" height="22"/><rect x="18" y="14" width="8" height="32"/><rect x="28" y="8" width="8" height="22"/><circle cx="36" cy="34" r="8"/><path d="M42 40l8 8"/></svg></div>
  <h3>Management consulting</h3><p>Pain can procure him some great pleasure. To take a trivial example, which of us ever takes</p>
</div>
<div class="abs service" style="left:601px">
  <div class="service-ring featured"><svg width="56" height="56" viewBox="0 0 56 56" fill="none" stroke="#e0531a" stroke-width="1.8"><rect x="10" y="12" width="32" height="32" rx="4"/><rect x="14" y="16" width="24" height="24" rx="2"/><path d="M19 28l6 6 22-22"/></svg></div>
  <h3>Hr and Strategy</h3><p>Pain can procure him some great pleasure. To take a trivial example, which of us ever takes</p>
</div>
<div class="abs service" style="left:862px">
  <div class="service-ring"><svg width="56" height="56" viewBox="0 0 56 56" fill="none" stroke="#555" stroke-width="1.6"><circle cx="28" cy="28" r="7"/><path d="M25 8h6l1 6 5 2 5-4 4 4-4 5 2 5 6 1v6l-6 1-2 5 4 5-4 4-5-4-5 2-1 6h-6l-1-6-5-2-5 4-4-4 4-5-2-5-6-1v-6l6-1 2-5-4-5 4-4 5 4 5-2z"/></svg></div>
  <h3>Selection System</h3><p>Pain can procure him some great pleasure. To take a trivial example, which of us ever takes</p>
</div>

<section class="abs band-grey"></section>
<h2 class="abs section-title" style="left:87px;top:1186px">WHY CHOOSE US</h2>
<div class="abs title-rule" style="left:87px;top:1228px;width:254px"></div>
<p class="abs why-text">Lorem Ipsum is simply dummy text of the printing and typesetting industry. Lorem Ipsum has been the industry's standard dummy text ever since the 1500s, when an unknown printer</p>
<ul class="abs check-list" style="left:86px;top:1322px">
  <li><span class="check"><svg width="9" height="9" viewBox="0 0 9 9"><path d="M1 4.5l2.3 2.3L8 2" fill="none" stroke="#fff" stroke-width="1.6"/></svg></span>Industry Expertise</li>
  <li><span class="check"><svg width="9" height="9" viewBox="0 0 9 9"><path d="M1 4.5l2.3 2.3L8 2" fill="none" stroke="#fff" stroke-width="1.6"/></svg></span>Guaranteed hire</li>
  <li><span class="check"><svg width="9" height="9" viewBox="0 0 9 9"><path d="M1 4.5l2.3 2.3L8 2" fill="none" stroke="#fff" stroke-width="1.6"/></svg></span>Best Customer Service</li>
</ul>
<ul class="abs check-list" style="left:285px;top:1326px">
  <li><span class="check"><svg width="9" height="9" viewBox="0 0 9 9"><path d="M1 4.5l2.3 2.3L8 2" fill="none" stroke="#fff" stroke-width="1.6"/></svg></span>Mass emailing</li>
  <li><span class="check"><svg width="9" height="9" viewBox="0 0 9 9"><path d="M1 4.5l2.3 2.3L8 2" fill="none" stroke="#fff" stroke-width="1.6"/></svg></span>Fixed Fee Model</li>
  <li><span class="check"><svg width="9" height="9" viewBox="0 0 9 9"><path d="M1 4.5l2.3 2.3L8 2" fill="none" stroke="#fff" stroke-width="1.6"/></svg></span>Multiple Hire</li>
</ul>
<a class="abs read-more">Read More &gt;&gt;</a>

<h2 class="abs section-title" style="left:562px;top:1186px">TESTIMONIALS</h2>
<div class="abs title-rule" style="left:562px;top:1228px;width:218px"></div>
<span class="abs quote-mark" style="left:550px;top:1238px">“</span>
<p class="abs quote">Lorem Ipsum is simply dummy text of the printing and typesetting industry. Lorem Ipsum has been the industry's standard dummy text ever since the 1500s, when an unknown printer took a galley of type and scrambled it to make a type specimen book...</p>
<span class="abs quote-mark" style="left:946px;top:1306px">”</span>
<div class="abs avatar" role="img" aria-label="Portrait of the client giving the testimonial"></div>
<div class="abs author"><strong>DANIEL HARTVIK</strong><span>Business man</span></div>
<div class="abs pager"><i></i><i></i></div>

<h2 class="abs section-title customers-title">OUR CUSTOMER</h2>
<div class="abs title-rule customers-rule"></div>
<svg class="abs carousel-arrow" style="left:46px" width="12" height="26" viewBox="0 0 12 26"><path d="M10 1L2 13l8 12" fill="none" stroke="#ccc" stroke-width="1.4"/></svg>
<div class="abs client" style="left:100px">Norvane</div>
<div class="abs client" style="left:305px">Quillpoint</div>
<div class="abs client" style="left:510px">Brightlattice</div>
<div class="abs client" style="left:716px">Tidewell</div>
<div class="abs client" style="left:921px">Corvexa</div>
<svg class="abs carousel-arrow" style="left:1140px" width="12" height="26" viewBox="0 0 12 26"><path d="M2 1l8 12-8 12" fill="none" stroke="#ccc" stroke-width="1.4"/></svg>

<section class="abs contact-band"></section>
<div class="abs contact-item" style="left:87px">
  <span class="contact-ring"><svg width="14" height="18" viewBox="0 0 14 18"><path d="M7 17s6-6.5 6-10.5a6 6 0 0 0-12 0C1 10.5 7 17 7 17z" fill="none" stroke="#fff" stroke-width="1.5"/><circle cx="7" cy="6.5" r="2" fill="#fff"/></svg></span>
  <span style="line-height:19px;font-size:12.5px">Relmo, 820 Harbor Crest Road Suite 14<br>Lakeview, NC 27501-4410</span>
</div>
<div class="abs contact-item" style="left:481px">
  <span class="contact-ring"><svg width="16" height="16" viewBox="0 0 16 16"><path d="M3 1.5l3 3-1.5 2a9 9 0 0 0 5 5l2-1.5 3 3-2 2C6 14 2 10 1.5 3.5z" fill="#fff"/></svg></span>
  <span>(555)-310-2280</span>
</div>
<div class="abs contact-item" style="left:732px">
  <span class="contact-ring"><svg width="16" height="16" viewBox="0 0 16 16"><rect x="2" y="5" width="12" height="9" rx="1" fill="none" stroke="#fff" stroke-width="1.4"/><rect x="5" y="2" width="6" height="4" fill="#fff"/><path d="M5 9h2M9 9h2M5 11.5h2M9 11.5h2" stroke="#fff"/></svg></span>
  <span>(555)-310-2280</span>
</div>
<div class="abs contact-item" style="left:985px">
  <span class="contact-ring"><svg width="16" height="12" viewBox="0 0 16 12"><rect x="1" y="1" width="14" height="10" rx="1" fill="none" stroke="#fff" stroke-width="1.4"/><path d="M1 1l7 6 7-6" fill="none" stroke="#fff" stroke-width="1.4"/></svg></span>
  <span>info@relmo.com</span>
</div>

<footer class="abs site-footer"></footer>
<div class="abs footer-brand"><span>Relmo</span><span class="brand-dot"></span></div>
<p class="abs footer-about">Es simplemente el texto de relleno de las imprentas y archivos de texto. Lorem Ipsum ha sido el texto de relleno estándar de las industrias desde el año 1500</p>

<div class="abs footer-divider" style="left:392px"></div>
<h4 class="abs footer-col-title" style="left:404px;top:1887px">QUICK LINKS</h4>
<div class="abs footer-col-rule" style="left:404px;top:1914px;width:122px"></div>
<ul class="abs footer-links" style="left:410px;top:1926px"><li>Home</li><li>About us</li><li>Services</li><li>Solutions</li><li>Options</li></ul>

<div class="abs footer-divider" style="left:598px"></div>
<h4 class="abs footer-col-title" style="left:630px;top:1887px">INFORMATION</h4>
<div class="abs footer-col-rule" style="left:630px;top:1914px;width:134px"></div>
<ul class="abs footer-links" style="left:632px;top:1926px"><li>Hr and Strategy</li><li>IT Recruitment</li><li>Management Consulting</li><li>Privacy Policy</li><li>Terms &amp; Condition</li></ul>

<div class="abs footer-divider" style="left:845px"></div>
<h4 class="abs footer-col-title" style="left:875px;top:1887px">CONTACT DETAILS</h4>
<div class="abs footer-col-rule" style="left:875px;top:1914px;width:180px"></div>
<div class="abs map" role="img" aria-label="Street map showing the office location"></div>

<div class="abs legal-bar"></div>
<p class="abs copyright">© Relmo 2016. All right reserved</p>
<div class="abs legal-social"><span class="social-dot"></span><span class="social-dot alt"></span><span class="social-dot"></span></div>

</body>
</html>
```